Custom Label for Essential Oils Bottle

We are a brand new company who specializes in seeking 100% pure essential oils. You would need to create a label that is similar to the designs attached, but unique to us. Our favorite label design is by quiet harbor blends. We really like how elegant their look is and would like to model that.
We will give the exact text of what we need put into the label to the winner after our favorite design is selected. Also, our logo is attached.
We would like the whole line to follow the same design with minor or tweaks for each scent (different color and text is all).
The label size would be 3" x 1.125" . There will be approximately 60 different oils in our first line but we only need 6 created for our first run.
Attached are the logo designs we really like.
Our first scent will be for a "Lemon" Essential oil bottle so design accordingly. The additional scents will be clove bud , peppermint, sweet orange, rosemary, and eucalyptus.
Thanks so much, and I look forward to seeing your designs!
Sam
Target Market(s)
Women, ages 18-65, wealthy
Industry/Entity Type
It Company

```html
<!DOCTYPE html>
<html lang="en">
<head>
<meta charset="utf-8">
<title>Lemon Essential Oil Label</title>
<link rel="stylesheet" href="https://fonts.googleapis.com/css2?family=Oswald:wght@400;500;600&display=swap">
<style>
  :root {
    --backdrop: #f1f0ec;
    --label-yellow: #f7ee1a;
    --label-yellow-edge: #e6d90c;
    --citrus-orange: #ec620c;
    --ink-black: #141414;
    --bloom-white: rgba(255, 255, 255, 0.85);
  }
  html, body {
    margin: 0;
    padding: 0;
    width: 914px;
    height: 1200px;
    overflow: hidden;
    background: var(--backdrop);
  }
  .canvas {
    position: relative;
    width: 914px;
    height: 1200px;
  }
  .label {
    position: absolute;
    left: 85px;
    top: 39px;
    width: 743px;
    height: 1122px;
    overflow: hidden;
    background: linear-gradient(90deg, var(--label-yellow-edge) 0%, var(--label-yellow) 18%, var(--label-yellow) 82%, var(--label-yellow-edge) 100%);
    font-family: "Oswald", "Arial Narrow", sans-serif;
  }
  .floral-art {
    position: absolute;
    left: 318px;
    top: 366px;
    width: 425px;
    height: 756px;
    background: radial-gradient(ellipse at 60% 45%, var(--bloom-white) 0%, rgba(255,255,255,0.45) 45%, rgba(255,255,255,0) 80%);
  }
  .scent-name {
    position: absolute;
    left: 58px;
    top: 150px;
    margin: 0;
    font-size: 262px;
    line-height: 1;
    font-weight: 400;
    color: var(--citrus-orange);
    letter-spacing: 2px;
  }
  .rule {
    position: absolute;
    left: 63px;
    width: 578px;
    height: 3px;
    background: var(--citrus-orange);
  }
  .rule-top { top: 420px; }
  .rule-mid { top: 510px; }
  .rule-low { top: 600px; }
  .detail {
    position: absolute;
    left: 66px;
    margin: 0;
    color: var(--citrus-orange);
    font-weight: 400;
    line-height: 1;
    letter-spacing: 1px;
  }
  .botanical-name { top: 428px; font-size: 72px; }
  .product-type { top: 530px; font-size: 52px; font-weight: 500; }
  .volume { top: 620px; font-size: 48px; font-weight: 500; }
  .brand-name {
    position: absolute;
    left: 63px;
    top: 800px;
    margin: 0;
    font-size: 104px;
    line-height: 1.02;
    font-weight: 600;
    color: var(--ink-black);
  }
</style>
</head>
<body>
  <div class="canvas">
    <section class="label">
      <div class="floral-art" role="img" aria-label="White line illustration of a lemon blossom branch"></div>
      <h1 class="scent-name">LEMON</h1>
      <div class="rule rule-top"></div>
      <p class="detail botanical-name">CIRTUS LEMON</p>
      <div class="rule rule-mid"></div>
      <p class="detail product-type">ESSENTIAL OIL</p>
      <div class="rule rule-low"></div>
      <p class="detail volume">15ML</p>
      <p class="brand-name">Luma<br>Grove</p>
    </section>
  </div>
</body>
</html>
```